Online trading school - Website design

We are building an online trading school (trading of shares, commodities, indices, currencies). The purpose is to teach online traders how to trade successfully. We need to design the homepage of the website and logo (bramwelloq.com will be the domain). The homepage will contain the following elements

- logo
- Sign in and Register links/buttons
- upper menu
- short introduction
- a couple of bullet points 'Why to join our school?'
- sign up form
- text
- bottom menu

Attached is a draft for the designer. The draft is just for an inspiration, the actual structure of the website can be different if the designer thinks so.

The designer is free to choose colors.

School

3 page

```html
<!DOCTYPE html>
<html lang="en">
<head>
<meta charset="utf-8">
<title>Bramwelloq – Online Trading School</title>
<link href="https://fonts.googleapis.com/css2?family=Montserrat:wght@400;500;600;700&display=swap" rel="stylesheet">
<style>
:root{
  --navy:#0e2a44;
  --navy-deep:#0b2035;
  --hero:#1f3e5e;
  --yellow:#f5d76e;
  --yellow-text:#f3cf5a;
  --button:#2c4a6e;
  --ink:#1b2a3a;
  --muted:#7a8088;
  --light:#f1f2f4;
  --white:#ffffff;
}
*{box-sizing:border-box;margin:0;padding:0}
html,body{width:756px;height:1200px;overflow:hidden}
body{position:relative;font-family:"Montserrat",sans-serif;background:var(--white);color:var(--ink)}
.abs{position:absolute}

.topbar{left:0;top:0;width:756px;height:29px;background:var(--navy);color:var(--white);font-size:9.5px;font-weight:600}
.topbar .follow{left:46px;top:9px}
.topbar .social{top:8px;width:13px;height:13px;background:#6d7f92;border-radius:2px}
.topbar .account{right:47px;top:9px}

.navbar{left:0;top:29px;width:756px;height:47px;background:var(--white)}
.brand{left:47px;top:13px;font-size:19px;font-weight:600;letter-spacing:.5px;color:var(--navy)}
.menu{top:17px;font-size:9.5px;color:var(--ink)}
.menu.active{color:var(--yellow-text)}
.menu-underline{left:331px;top:44px;width:74px;height:3px;background:var(--yellow)}

.hero{left:0;top:76px;width:756px;height:429px;background:linear-gradient(120deg,#2a4a6c 0%,#1c3a59 45%,#17324f 100%)}
.intro{left:46px;top:200px;width:320px;height:164px;border-left:2px solid var(--white);padding-left:20px;color:var(--white)}
.intro h1{font-size:22px;font-weight:700;line-height:27px;margin-top:2px}
.intro p{font-size:9.3px;line-height:14px;margin-top:17px;font-weight:500}
.intro a{display:inline-block;margin-top:22px;margin-left:2px;font-size:9.5px;font-weight:600;color:var(--yellow-text);text-decoration:underline}

.signup{left:435px;top:120px;width:273px;height:337px;background:var(--yellow);border-radius:2px;padding:22px 24px}
.signup h2{font-size:20px;font-weight:700;color:#23436a;letter-spacing:.3px}
.signup .sub{font-size:11px;color:var(--navy);margin-top:4px}
.field{position:absolute;background:var(--white);border-radius:2px;font-size:8.5px;color:#9aa0a8;padding:12px 17px}
.apply{position:absolute;left:21px;top:271px;width:228px;height:30px;background:var(--button);color:var(--white);font-size:10.5px;font-weight:700;text-align:center;line-height:30px;border-radius:2px}

.feature-icon{width:40px;height:40px;background:var(--yellow);border-radius:2px;display:flex;align-items:center;justify-content:center}
.feature h3{font-size:10.5px;font-weight:500;color:var(--ink)}
.feature p{font-size:8.6px;line-height:14px;color:var(--muted);margin-top:9px;width:150px}

.join{left:500px;top:682px;width:209px;height:58px;background:var(--yellow);box-shadow:0 2px 6px rgba(0,0,0,.18);font-size:16px;font-weight:500;color:var(--navy);text-align:center;line-height:58px;letter-spacing:.5px}

.offer{left:0;top:793px;width:756px;height:348px;background:var(--light)}
.offer .eyebrow{left:46px;top:80px;font-size:11px;color:var(--yellow-text);letter-spacing:.3px}
.offer h2{left:46px;top:110px;font-size:16.5px;font-weight:500;line-height:20px;color:var(--ink)}
.offer p{left:46px;top:166px;width:250px;font-size:8.6px;line-height:14px;color:var(--muted)}
.photo{border-radius:0}

.footer{left:0;top:1141px;width:756px;height:59px;background:var(--navy-deep);color:var(--white);font-size:9px;font-weight:500}
.footer .copy{left:46px;top:24px}
.footer .links{right:47px;top:24px}
</style>
</head>
<body>

<header class="abs topbar">
  <span class="abs follow">FOLLOW US</span>
  <span class="abs social" style="left:114px"></span>
  <span class="abs social" style="left:139px"></span>
  <span class="abs social" style="left:165px"></span>
  <span class="abs account">SIGN IN &nbsp;|&nbsp; REGISTER</span>
</header>

<nav class="abs navbar">
  <span class="abs brand">BRAMWELLOQ</span>
  <span class="abs menu active" style="left:331px">About our school</span>
  <span class="abs menu" style="left:438px">Risk warning</span>
  <span class="abs menu" style="left:523px">FAQ</span>
  <span class="abs menu" style="left:569px">Trading Glossary</span>
  <span class="abs menu" style="left:672px">Contact</span>
  <span class="abs menu-underline"></span>
</nav>

<section class="abs hero" role="img" aria-label="Dark blue toned photo of a smiling man in the background"></section>

<div class="abs intro">
  <h1>WELCOME TO<br>BRAMWELLOQ</h1>
  <p>Lorem Ipsum is simply dummy text of the printing and typesetting industry. Lorem Ipsum has been the industry's standard dummy text ever since the 1500s, when an unknown printer took a galley of type and scrambled it to make a type</p>
  <a>LEARN MORE</a>
</div>

<form class="abs signup">
  <h2>BECOME A MEMBER</h2>
  <div class="sub">Join our school now !</div>
  <div class="field" style="left:21px;top:83px;width:110px;height:29px">First Name</div>
  <div class="field" style="left:138px;top:83px;width:111px;height:29px">Last Name</div>
  <div class="field" style="left:21px;top:119px;width:228px;height:29px">Email Address</div>
  <div class="field" style="left:21px;top:155px;width:228px;height:29px">Select Learning Program</div>
  <div class="field" style="left:21px;top:191px;width:228px;height:67px">Additional Information</div>
  <div class="apply">APPLY NOW</div>
</form>

<div class="abs feature-icon" style="left:46px;top:572px">
  <svg width="24" height="24" viewBox="0 0 24 24" fill="none" stroke="#fff" stroke-width="1.6"><circle cx="12" cy="12" r="10"/><circle cx="12" cy="12" r="6"/><circle cx="12" cy="12" r="2"/><path d="M12 12l8-8"/></svg>
</div>
<div class="abs feature" style="left:103px;top:571px"><h3>Best trading tips ever</h3><p>Morbi leo risus, porta ac consectetur, vestibulum at eros. Vivamus sagittis lacus vel augue</p></div>

<div class="abs feature-icon" style="left:273px;top:572px">
  <svg width="24" height="24" viewBox="0 0 24 24" fill="#fff"><circle cx="12" cy="4" r="3"/><rect x="7" y="9" width="10" height="3"/><rect x="3" y="11" width="3" height="10"/><rect x="18" y="11" width="3" height="10"/><rect x="10" y="12" width="4" height="9"/></svg>
</div>
<div class="abs feature" style="left:330px;top:571px"><h3>Secret tips from experts</h3><p>Morbi leo risus, porta ac consectetur, vestibulum at eros. Vivamus sagittis lacus vel augue</p></div>

<div class="abs feature-icon" style="left:500px;top:572px">
  <svg width="24" height="24" viewBox="0 0 24 24" fill="#fff"><rect x="3" y="16" width="3" height="6"/><rect x="8" y="13" width="3" height="9"/><rect x="13" y="15" width="3" height="7"/><rect x="18" y="10" width="3" height="12"/><path d="M3 13l6-5 4 3 7-7" stroke="#fff" stroke-width="1.6" fill="none"/></svg>
</div>
<div class="abs feature" style="left:557px;top:571px"><h3>Learn how to trade online</h3><p>Morbi leo risus, porta ac consectetur, vestibulum at eros. Vivamus sagittis lacus vel augue</p></div>

<div class="abs feature-icon" style="left:46px;top:682px">
  <svg width="24" height="24" viewBox="0 0 24 24" fill="none" stroke="#fff" stroke-width="1.6"><circle cx="12" cy="5" r="3"/><circle cx="5" cy="18" r="3"/><circle cx="19" cy="18" r="3"/><path d="M12 8v4M12 12l-5 4M12 12l5 4"/></svg>
</div>
<div class="abs feature" style="left:103px;top:681px"><h3>How to trade commodities</h3><p>Morbi leo risus, porta ac consectetur, vestibulum at eros. Vivamus sagittis lacus vel augue</p></div>

<div class="abs feature-icon" style="left:273px;top:682px">
  <svg width="24" height="24" viewBox="0 0 24 24" fill="none" stroke="#fff" stroke-width="1.8" stroke-linejoin="round"><path d="M2 12l5-5 5 2 5-2 5 5-8 7z"/><path d="M9 12l3 3"/></svg>
</div>
<div class="abs feature" style="left:330px;top:681px"><h3>Learn how to become a trader</h3><p>Morbi leo risus, porta ac consectetur, vestibulum at eros. Vivamus sagittis lacus vel augue</p></div>

<div class="abs join">JOIN US NOW !</div>

<section class="abs offer">
  <span class="abs eyebrow">WHAT DO WE OFFER ?</span>
  <h2 class="abs">EDUCATION IS THE<br>MOST POWERFUL WEAPON</h2>
  <p class="abs">There are many variations of passages of Lorem Ipsum available, but the majority have suffered alteration in some form, by injected humour, or randomised words which don't look even slightly believable. If you are going to use a passage of Lorem Ipsum, you need to be sure there isn't anything embarrassing hidden in the middle of text.</p>
</section>

<div class="abs photo" style="left:386px;top:858px;width:153px;height:222px;background:linear-gradient(160deg,#8a7a5e,#cdb98f 50%,#e9e4dc)" role="img" aria-label="Photo of a student with glasses reading a tablet"></div>
<div class="abs photo" style="left:556px;top:858px;width:153px;height:102px;background:linear-gradient(180deg,#b9bcc0,#d7d8da)" role="img" aria-label="Photo of two women studying at laptops"></div>
<div class="abs photo" style="left:556px;top:978px;width:153px;height:102px;background:linear-gradient(120deg,#cbb9a0,#6d7d93 70%,#e3e0da)" role="img" aria-label="Photo of a man with glasses thinking at a laptop"></div>

<footer class="abs footer">
  <span class="abs copy">Copyright 2016 . All rights reserved</span>
  <span class="abs links">Terms and Conditions &nbsp;&nbsp;|&nbsp;&nbsp; Privacy Protection</span>
</footer>

</body>
</html>
```